Business cards for Norwegian software consultancy business

We are in need of business cards for our Norwegian consultancy company.
“Vilma Tronsoft AS” specializes in software development, architecture and agile methodology, providing mostly on-site services at customers.
The cards should reflect a certain level of business professionalism with an elegant touch, while paying tribute to our modern and technological heritage. Our logo should be featured, as well as room for basic information about the cardholder and legal information of the company (company name, address and VAT number).
We would like our cards to reflect that we are a modern consulting company. It should present a professional image that people will remember. The texture and color pallette should reflect our professionalism and reliability, so we prefer a light color pallette with colors such as gray, white, blue and black. The number of colors used should however not be overwhelming, with the text being distinct and readable.
We are open to untraditional layouts and playful designs as long as they communicate the intent stated above.
You could also take a look at our website http://www.tronsoft-demo.no for input on our visual profile.
Our logo is attached in the form of vectors and rasterized PNG. Please comment if you would like the black-white and/or inverted versions as well.
Architecture
Company information:
Vilma Tronsoft AS
Lindåsgata 7, 3129 Nøtterøy
481 62 509
info@tronsoft-demo.no
www.tronsoft-demo.no
Employee information:
Full name
Title
Email
Phone

```html
<!DOCTYPE html>
<html lang="en">
<head>
<meta charset="utf-8">
<title>Vilma Tronsoft AS – Business Cards</title>
<link rel="stylesheet" href="https://fonts.googleapis.com/css2?family=Arimo:wght@400;700&family=Roboto+Condensed:wght@700&display=swap">
<style>
  :root {
    --bg-top: #9aa3a3;
    --bg-bottom: #5f6868;
    --card-black: #000000;
    --card-blue: #84b6dc;
    --card-blue-deep: #6fa6d2;
    --accent-blue: #7fb3e0;
    --white: #ffffff;
    --ink: #111418;
  }
  * { box-sizing: border-box; margin: 0; padding: 0; }
  html, body { width: 1200px; height: 900px; overflow: hidden; }
  body {
    background: radial-gradient(ellipse at 50% 40%, var(--bg-top), var(--bg-bottom));
    font-family: "Arimo", Arial, sans-serif;
    position: relative;
  }
  .card {
    position: absolute;
    width: 560px;
    height: 320px;
    border-radius: 26px;
    overflow: hidden;
    box-shadow: 0 14px 30px rgba(0,0,0,.35);
  }
  .divider {
    position: absolute;
    top: 0; bottom: 0;
    width: 2px;
    background: var(--white);
  }

  /* Front: black card with cardholder details */
  .card-front {
    left: 560px; top: 90px;
    background: var(--card-black);
  }
  .card-front .divider { left: 320px; }
  .holder {
    position: absolute;
    left: 346px; top: 34px;
    color: var(--accent-blue);
    font-size: 15px;
    line-height: 1.3;
  }
  .holder-name { font-size: 16px; }
  .holder-title { font-weight: 700; font-size: 16px; margin-bottom: 4px; }
  .contact-line { display: flex; align-items: center; gap: 7px; }
  .contact-line svg { width: 12px; height: 12px; flex: none; }
  .address { font-weight: 700; font-size: 13px; margin-top: 2px; }
  .wordmark {
    position: absolute;
    display: flex; align-items: center; gap: 10px;
    color: var(--white);
    font-weight: 400;
    white-space: nowrap;
  }
  .wordmark-square { background: var(--accent-blue); flex: none; }
  .card-front .wordmark {
    right: 258px; bottom: 70px;
    font-size: 24px;
  }
  .card-front .wordmark-square { width: 16px; height: 16px; }

  /* Back: blue card with company line */
  .card-back {
    left: 80px; top: 480px;
    background: linear-gradient(180deg, var(--card-blue), var(--card-blue-deep));
  }
  .card-back .divider { left: 346px; }
  .card-back .wordmark {
    left: 372px; top: 40px;
    color: var(--ink);
    font-size: 26px;
    flex-direction: column; align-items: flex-start; gap: 8px;
    line-height: 1.05;
  }
  .card-back .wordmark-square { width: 30px; height: 30px; background: var(--white); }
  .tagline {
    position: absolute;
    right: 236px; top: 200px;
    text-align: right;
    font-family: "Roboto Condensed", "Arial Narrow", sans-serif;
    font-weight: 700;
    font-size: 11px;
    letter-spacing: .2px;
    line-height: 1.35;
    color: var(--ink);
    text-transform: uppercase;
  }
</style>
</head>
<body>

<section class="card card-front" aria-label="Business card front">
  <div class="divider"></div>
  <div class="wordmark"><span class="wordmark-square"></span>Vilma Tronsoft</div>
  <div class="holder">
    <p class="holder-name">Ola Brennvik</p>
    <p class="holder-title">Co-Founder &amp; CEO</p>
    <p class="contact-line">
      <svg viewBox="0 0 12 12" aria-hidden="true"><rect x="3" y="0.5" width="6" height="11" rx="1" fill="none" stroke="currentColor"/><line x1="5" y1="9.5" x2="7" y2="9.5" stroke="currentColor"/></svg>
      (047) 555-0192
    </p>
    <p class="contact-line">
      <svg viewBox="0 0 12 12" aria-hidden="true"><rect x="0.5" y="2" width="11" height="8" fill="none" stroke="currentColor"/><polyline points="0.5,2 6,7 11.5,2" fill="none" stroke="currentColor"/></svg>
      info@tronsoft-demo.no
    </p>
    <p class="contact-line">
      <svg viewBox="0 0 12 12" aria-hidden="true"><circle cx="6" cy="6" r="5.3" fill="none" stroke="currentColor"/><ellipse cx="6" cy="6" rx="2.2" ry="5.3" fill="none" stroke="currentColor"/><line x1="0.7" y1="6" x2="11.3" y2="6" stroke="currentColor"/></svg>
      tronsoft-demo.no
    </p>
    <p class="address">Lindåsgata 7<br>3129 Nøtterøy</p>
  </div>
</section>

<section class="card card-back" aria-label="Business card back">
  <div class="divider"></div>
  <div class="wordmark"><span class="wordmark-square"></span>Vilma<br>Tronsoft</div>
  <p class="tagline">Rental of qualified resources in software development<br>project management and IT operations</p>
</section>

</body>
</html>
```